Meridian Handsets business card design

I would like to see some designs for a business card for Meridian Handsets. I would like the business card to be double sided. It will need to have a similar colour / look and feel to our website www.meridianhandsets.com.au I have also attached our latest flyer. Final designs to be handed over in Photoshop format so that I can edit the business card when needed please.

Industry/Entity Type

Business

Contact Information for Business Card

Gavin Thornley
sales@meridianhandsets.com.au
Business Development Manager
ph: (08) 6197 5821
www.meridianhandsets.com.au

Font styles to use
Serif
Sans Serif

Requirements
Must have
• If you could please utilise our colour scheme as seen on our website and the attached flyer.
• I would also like the final design to be in a Photoshop format so that I can edit it when needed please.

```html
<!DOCTYPE html>
<html lang="en">
<head>
<meta charset="utf-8">
<title>Meridian Handsets – Business Card</title>
<link rel="stylesheet" href="https://fonts.googleapis.com/css2?family=Source+Sans+3:ital,wght@0,400;0,600;0,700;1,400;1,600;1,700&display=swap">
<style>
  :root {
    --brand-blue: #0a7db9;
    --card-white: #ffffff;
    --ink: #333333;
    --backdrop: #444444;
    --on-blue: #ffffff;
  }
  * { margin: 0; padding: 0; box-sizing: border-box; }
  html, body {
    width: 1105px;
    height: 1200px;
    overflow: hidden;
  }
  body {
    background: var(--backdrop);
    font-family: "Source Sans 3", sans-serif;
    position: relative;
  }
  .card {
    position: absolute;
    left: 196px;
    width: 720px;
    height: 413px;
  }
  .card--front {
    top: 145px;
    background: var(--card-white);
  }
  .card--back {
    top: 602px;
    background: var(--brand-blue);
  }
  .brand-name {
    position: absolute;
    top: 44px;
    right: 39px;
    font-size: 38px;
    font-weight: 600;
    color: var(--brand-blue);
    letter-spacing: -0.3px;
    white-space: nowrap;
  }
  .contact {
    position: absolute;
    left: 43px;
    top: 231px;
    color: var(--ink);
  }
  .contact__name {
    font-size: 28px;
    font-weight: 600;
    color: var(--brand-blue);
    line-height: 1.1;
  }
  .contact__title {
    font-size: 20px;
    line-height: 1.35;
    margin-bottom: 10px;
  }
  .contact__line {
    font-size: 18px;
    line-height: 27px;
  }
  .contact__label {
    color: var(--brand-blue);
    font-weight: 700;
    font-style: italic;
  }
  .back-brand {
    position: absolute;
    top: 150px;
    left: 0;
    right: 0;
    display: flex;
    align-items: center;
    justify-content: center;
    gap: 18px;
    color: var(--on-blue);
    font-size: 40px;
    font-weight: 600;
  }
  .back-brand__dot {
    width: 22px;
    height: 22px;
    border-radius: 50%;
    background: var(--on-blue);
  }
  .back-url {
    position: absolute;
    top: 347px;
    left: 0;
    right: 0;
    text-align: center;
    color: var(--on-blue);
    font-size: 18px;
    font-style: italic;
    letter-spacing: 3px;
  }
  .back-url strong { font-weight: 700; }
</style>
</head>
<body>
  <section class="card card--front">
    <div class="brand-name">Meridian Handsets</div>
    <div class="contact">
      <p class="contact__name">Gavin Thornley</p>
      <p class="contact__title">Business Development Manager</p>
      <p class="contact__line"><span class="contact__label">Phone:</span> (08) 6197 5821</p>
      <p class="contact__line">sales@meridianhandsets.com.au</p>
      <p class="contact__line">www.meridianhandsets.com.au</p>
    </div>
  </section>

  <section class="card card--back">
    <div class="back-brand">
      <span class="back-brand__dot"></span>
      <span>Meridian Handsets</span>
    </div>
    <p class="back-url">www.<strong>meridianhandsets</strong>.com.au</p>
  </section>
</body>
</html>
```